Magician | Speaker looks for an innovative business card design

I'm a magician and public speaker offering artistic and modern magical experiences.
I'm based in Brussels (Belgium.) I love magic performed up-close, creating a space of intimacy, even when I'm on stage.
The final design should communicate professionalism, elegance, artistry, and a friendly kind personality

I would like to see designs based either on my photos and/or the way I sign my name Remy Vok (see attached files for more info.)
Additional photos and more info about what I offer can be seen at www.remy-vok.net

My current business card design is also attached. I like the fact that the reverse of my current design includes quotes from master magicians about magic, changing the way my participants see the art of magic.

Note: I would like a double-sided card design. However, I need white space on the reverse to be able to write things on for my performances.

Details to include on the card:
Artist name: Remy Vok
Offer: magician + (public) speaker or magic + (public) speaking (the + sign can be replaced by another character, like a bullet or a pipe)
Phone: +32 471 265 903
Email: book@remy-vok.net
(optional) Website: www.remy-vok.net or remy-vok.net

Target Market(s)

Corporate, organisations, companies as well as individuals

Industry/Entity Type

Artists

Colors

Designer to choose colors to be used in the design.

Requirements
Nice to have
• A side with a mirror could be nice

```html
<!DOCTYPE html>
<html lang="en">
<head>
<meta charset="utf-8">
<title>Remy Vok – Business Card</title>
<link rel="stylesheet" href="https://fonts.googleapis.com/css2?family=Allura&family=Arimo:wght@400&display=swap">
<style>
  :root {
    --page: #ffffff;
    --card: #000000;
    --gold: #c9a06a;
    --gold-dark: #8f6a3e;
    --gold-light: #f3d3a0;
    --shadow: rgba(0, 0, 0, 0.28);
  }
  * { margin: 0; padding: 0; box-sizing: border-box; }
  html, body { width: 1200px; height: 1021px; overflow: hidden; background: var(--page); }
  .canvas { position: relative; width: 1200px; height: 1021px; }
  .card-shapes { position: absolute; left: 0; top: 0; }
  .card-shape { fill: var(--card); filter: drop-shadow(0 6px 8px var(--shadow)); }

  .artist-name {
    position: absolute;
    right: 360px;
    top: 196px;
    font-family: "Allura", cursive;
    font-size: 58px;
    line-height: 1;
    color: var(--gold);
  }
  .offer-line {
    position: absolute;
    right: 360px;
    top: 300px;
    font-family: "Allura", cursive;
    font-size: 32px;
    line-height: 1;
    color: var(--gold);
  }
  .offer-bar {
    position: absolute;
    left: 600px;
    top: 340px;
    width: 240px;
    height: 26px;
    background: linear-gradient(90deg, var(--gold-dark), var(--gold-light) 55%, var(--gold-dark));
  }
  .contact-list { position: absolute; left: 369px; top: 362px; list-style: none; }
  .contact-item {
    display: flex;
    align-items: center;
    height: 28px;
    margin-bottom: 6px;
    font-family: "Arimo", sans-serif;
    font-size: 16px;
    color: var(--gold);
  }
  .contact-icon {
    width: 28px;
    height: 28px;
    margin-right: 12px;
    border: 1.5px solid var(--gold);
    padding: 2px;
  }
  .contact-icon svg { display: block; width: 100%; height: 100%; }

  .back-name {
    position: absolute;
    left: 313px;
    width: 574px;
    top: 650px;
    text-align: center;
    font-family: "Allura", cursive;
    font-size: 64px;
    line-height: 1;
    color: var(--gold);
  }
  .back-offer {
    position: absolute;
    left: 313px;
    width: 574px;
    top: 755px;
    text-align: center;
    font-family: "Allura", cursive;
    font-size: 17px;
    line-height: 19px;
    color: var(--gold);
  }
</style>
</head>
<body>
<main class="canvas">
  <svg class="card-shapes" width="1200" height="1021" viewBox="0 0 1200 1021" aria-hidden="true">
    <path class="card-shape card-front" d="M353,190 L847,145 Q887,141 887,181 L887,457 Q887,497 847,497 L353,497 Q313,497 313,457 L313,230 Q313,193 353,190 Z"/>
    <path class="card-shape card-back" d="M353,523 L847,570 Q887,574 887,614 L887,837 Q887,877 847,877 L353,877 Q313,877 313,837 L313,563 Q313,523 353,523 Z"/>
  </svg>

  <section class="card-front-content">
    <h1 class="artist-name">Remy Vok</h1>
    <p class="offer-line">magician - speaker</p>
    <div class="offer-bar"></div>
    <ul class="contact-list">
      <li class="contact-item">
        <span class="contact-icon"><svg viewBox="0 0 20 20"><rect width="20" height="20" fill="#b88c56"/><path d="M5,4 L8,4 L9,7 L7.5,8.5 Q9,11.5 11.5,12.5 L13,11 L16,12 L16,15 Q10,16 5,10 Q4,7 5,4 Z" fill="#fff"/></svg></span>
        +32 471 265 903
      </li>
      <li class="contact-item">
        <span class="contact-icon"><svg viewBox="0 0 20 20"><rect width="20" height="20" fill="#b88c56"/><rect x="4" y="6" width="12" height="8" fill="none" stroke="#fff" stroke-width="1.2"/><path d="M4,6 L10,11 L16,6" fill="none" stroke="#fff" stroke-width="1.2"/></svg></span>
        book@remy-vok.net
      </li>
      <li class="contact-item">
        <span class="contact-icon"><svg viewBox="0 0 20 20"><rect width="20" height="20" fill="#b88c56"/><circle cx="10" cy="10" r="6" fill="none" stroke="#fff" stroke-width="1.2"/><ellipse cx="10" cy="10" rx="2.5" ry="6" fill="none" stroke="#fff" stroke-width="1"/><path d="M4,10 H16" stroke="#fff" stroke-width="1"/></svg></span>
        www.remy-vok.net or remy-vok.net
      </li>
    </ul>
  </section>

  <section class="card-back-content">
    <p class="back-name">Remy Vok</p>
    <p class="back-offer">magician + (public) speaker,<br>magic + (public) speaking</p>
  </section>
</main>
</body>
</html>
```